VELMOR Website Design

We need a website designed for our company VELMOR. We are a luxury lifestyle club that will provide benefits and services for our members. The site should be clean & sleek, preferably using black and white (or darker colors). (example sites: brastelle.com, fovix.com)

Here is a link of a sample page I did using wix. (https://dunmerel7.pagebuildr.com/mysite) This can be used to get a general idea.

Target Market(s)

Upper Middle Class in the United States

Number of Pages Required

5+ page

Font styles to use
Sans Serif
Other font styles liked:
• Arial (or other similar fonts)

Requirements
Must have
• A clean design that is eye-catching and speaks to our company.
Nice to have
• Ideas for copy.

```html
<!DOCTYPE html>
<html lang="en">
<head>
<meta charset="utf-8">
<title>VELMOR</title>
<link rel="stylesheet" href="https://fonts.googleapis.com/css2?family=Montserrat:wght@500;600;700&family=Roboto:wght@300;400;500&display=swap">
<style>
:root{
  --cyan:#17c1ee;
  --ink:#333436;
  --muted:#666;
  --soft:#888;
  --line:#ececec;
  --night:#212224;
  --field:#3c3d40;
  --rule:#37383b;
  --paper:#ffffff;
  --pale:#c9c9cb;
}
*{box-sizing:border-box;margin:0;padding:0}
html,body{width:1200px;height:1097px;overflow:hidden;background:var(--paper)}
body{position:relative;font-family:"Roboto",Arial,sans-serif}
.abs{position:absolute}

.news-title{left:0;width:1200px;top:54px;text-align:center;font:700 34px/40px "Montserrat",sans-serif;color:var(--ink)}
.nav-btn{top:122px;width:35px;height:35px;border-radius:50%;display:flex;align-items:center;justify-content:center}
.nav-prev{left:560px;border:1.5px solid #d3d3d3}
.nav-next{left:605px;background:var(--cyan)}

.card{top:191px;width:290px;height:396px;border:1px solid var(--line);background:var(--paper);text-align:center}
.card.featured{box-shadow:0 12px 28px rgba(0,0,0,.08)}
.card-media{height:171px;width:100%}
.media-1{background:radial-gradient(ellipse at 40% 30%,#f5f0ff 0%,#9f8fd8 20%,#3a4fa0 50%,#121a30 85%)}
.media-2{background:radial-gradient(circle at 75% 20%,#ff4fa8 0%,#6a2ad0 30%,#1b2a9e 60%,#0c1240 100%)}
.media-3{background:radial-gradient(ellipse at 50% 30%,#b7d8ff 0%,#4a6fb8 25%,#1d4048 55%,#13302b 100%)}
.card-date{margin-top:22px;font:300 12px/16px "Roboto",sans-serif;color:var(--soft)}
.card-title{margin:6px 22px 0;font:600 14.5px/20px "Montserrat",sans-serif;color:var(--ink)}
.card-text{margin:10px 22px 0;font:300 13px/21px "Roboto",sans-serif;color:var(--muted)}
.card-btn{display:inline-block;margin-top:19px;width:97px;height:32px;border:1.5px solid var(--cyan);border-radius:2px;font:500 13px/29px "Roboto",sans-serif;color:var(--cyan)}
.featured .card-btn{background:var(--cyan);color:#fff;height:30px;width:95px;margin-top:20px;line-height:28px}

.dark{left:0;top:664px;width:1200px;height:433px;background:var(--night)}
.nl-title{left:131px;top:702px;font:700 26px/32px "Montserrat",sans-serif;color:#fff}
.nl-text{left:131px;top:740px;width:470px;font:300 14px/21px "Roboto",sans-serif;color:#b9babc}
.nl-form{left:670px;top:722px;width:398px;height:46px;background:var(--field);border-radius:2px}
.nl-field{left:17px;top:0;font:400 13.5px/46px "Roboto",sans-serif;color:#b7b8ba}
.nl-submit{left:284px;top:4px;width:110px;height:38px;background:var(--cyan);border-radius:2px;text-align:center;font:500 13px/38px "Roboto",sans-serif;color:#fff}
.rule-top{left:0;top:822px;width:1200px;height:1px;background:var(--rule)}

.brand{left:130px;top:852px;font:500 36px/40px "Montserrat",sans-serif;color:#fff;letter-spacing:.5px}
.contact{left:131px;font:400 13px/18px "Roboto",sans-serif;color:#d8d8d8}
.contact a,.event-time{color:var(--cyan);text-decoration:none}
.col-head{top:857px;font:700 14.5px/18px "Montserrat",sans-serif;color:var(--cyan)}
.link{left:388px;font:400 12px/16px "Roboto",sans-serif;color:#cfd0d2}
.event{left:618px;font:400 12px/16px "Roboto",sans-serif;color:#cfd0d2}
.event-time{left:618px;font:400 12px/16px "Roboto",sans-serif}
.social{top:900px;width:30px;height:30px;border-radius:50%;background:#8d8e90}
.rule-bottom{left:131px;top:1028px;width:937px;height:1px;background:var(--rule)}
.copy{left:0;width:1200px;top:1052px;text-align:center;font:400 13px/16px "Roboto",sans-serif;color:#b2b3b5}
</style>
</head>
<body>
<h2 class="abs news-title">LATEST NEWS</h2>
<div class="abs nav-btn nav-prev"><svg width="16" height="16" viewBox="0 0 16 16"><path d="M14 8H2M7 3L2 8l5 5" fill="none" stroke="#c9c9c9" stroke-width="1.8" stroke-linecap="round" stroke-linejoin="round"/></svg></div>
<div class="abs nav-btn nav-next"><svg width="16" height="16" viewBox="0 0 16 16"><path d="M2 8h12M9 3l5 5-5 5" fill="none" stroke="#fff" stroke-width="2" stroke-linecap="round" stroke-linejoin="round"/></svg></div>

<article class="abs card" style="left:132px">
  <div class="card-media media-1" role="img" aria-label="Concert crowd with raised hands under stage lights"></div>
  <p class="card-date">July 27th, 2018</p>
  <h3 class="card-title">Nulla eget molestie massa eleifen velit nulla facilisiulla</h3>
  <p class="card-text">Phasellus tellus risus, tincidunt eu scelerisque a, blandit sed metus. Aliquam ut tristique mi fusce vitae dignissim.</p>
  <span class="card-btn">READ MORE</span>
</article>
<article class="abs card featured" style="left:455px">
  <div class="card-media media-2" role="img" aria-label="Nightclub dance floor lit in blue and pink"></div>
  <p class="card-date">July 27th, 2018</p>
  <h3 class="card-title">Nulla eget molestie massa eleifen velit nulla facilisiulla</h3>
  <p class="card-text">Phasellus tellus risus, tincidunt eu scelerisque a, blandit sed metus. Aliquam ut tristique mi fusce vitae dignissim.</p>
  <span class="card-btn">READ MORE</span>
</article>
<article class="abs card" style="left:778px">
  <div class="card-media media-3" role="img" aria-label="Lounge room with a light projector casting patterns on the ceiling"></div>
  <p class="card-date">July 27th, 2018</p>
  <h3 class="card-title">Nulla eget molestie massa eleifen velit nulla facilisiulla</h3>
  <p class="card-text">Phasellus tellus risus, tincidunt eu scelerisque a, blandit sed metus. Aliquam ut tristique mi fusce vitae dignissim.</p>
  <span class="card-btn">READ MORE</span>
</article>

<div class="abs dark"></div>
<h2 class="abs nl-title">SUBSCRIPTION NEWSLETTER</h2>
<p class="abs nl-text">Phasellus tellus risus, tincidunt eu scelerisque a, blandit sed metus. Aliquam ut tristique mi. Fusce vitae dignissim enim. Nam tincidunt dictum libero sed.</p>
<div class="abs nl-form">
  <span class="abs nl-field">ENTER EMAIL</span>
  <span class="abs nl-submit">SUBSCRIBE</span>
</div>
<div class="abs rule-top"></div>

<div class="abs brand">VELMOR</div>
<p class="abs contact" style="top:902px">Call: <a href="#">555-014-2390</a></p>
<p class="abs contact" style="top:926px">Email: <a href="#">info@velmor.com</a></p>

<h4 class="abs col-head" style="left:388px">LINKS</h4>
<span class="abs link" style="top:898px">Home</span>
<span class="abs link" style="top:922px">About</span>
<span class="abs link" style="top:946px">Services &amp; Benefits</span>
<span class="abs link" style="top:970px">Contact</span>

<h4 class="abs col-head" style="left:618px">EVENT DATES</h4>
<span class="abs event" style="top:898px">Monday to Friday</span>
<span class="abs event-time" style="top:916px">06PM-11PM</span>
<span class="abs event" style="top:945px">Saturday to Sunday</span>
<span class="abs event-time" style="top:963px">9PM-01AM</span>

<h4 class="abs col-head" style="left:840px">FOLLOW US</h4>
<span class="abs social" style="left:841px"></span>
<span class="abs social" style="left:874px"></span>
<span class="abs social" style="left:908px"></span>

<div class="abs rule-bottom"></div>
<p class="abs copy">2018 © Copyright, VELMOR, All Rights Reserved</p>
</body>
</html>
```